Criação de Kit Layout de Posts para Redes Sociais (Facebook, Instagram e etc) para Advocacia e Direito
" Prestamos assessoria para os clientes saberem sua situação atual, perante a Previdência Social, e fazemos um planejamento previdenciário, com acompanhamento até a concessão do benefício pretendido, seja pela via administrativa, seja pela via judicial. Assim, realizamos contagem de tempo de contribuição, simulação de valor de benefício, planejamento previdenciário, requerimento administrativo e ajuizamento de ação judicial, tudo para o fim de obter a concessão de Aposentadoria, revisão de benefício, Auxílio-Doença, Auxílio-Acidente, Salário-Maternidade, Pensão por morte, Auxílio-Reclusão e Benefício Assistencial. "

```html
<!DOCTYPE html>
<html lang="pt-BR">
<head>
<meta charset="UTF-8">
<title>Pensão por Morte: quem tem direito?</title>
<link rel="stylesheet" href="https://fonts.googleapis.com/css2?family=Open+Sans:wght@400;600;700&display=swap">
<style>
  :root {
    --navy: #0f2146;
    --navy-deep: #0a1836;
    --gold: #c7a06a;
    --ink: #2b2b2b;
    --title: #1c3357;
    --white: #ffffff;
  }
  html, body {
    margin: 0;
    padding: 0;
    width: 1200px;
    height: 1200px;
    overflow: hidden;
    background: var(--white);
  }
  .post {
    position: relative;
    width: 1200px;
    height: 1200px;
    overflow: hidden;
    font-family: "Open Sans", Arial, sans-serif;
  }
  .backdrop {
    position: absolute;
    inset: 0;
    background:
      radial-gradient(ellipse 520px 420px at 640px 760px, rgba(226,186,160,0.75), rgba(226,186,160,0) 70%),
      radial-gradient(ellipse 700px 500px at 300px 140px, rgba(198,160,104,0.55), rgba(198,160,104,0) 70%),
      linear-gradient(180deg, #eef1ee 0%, #f2f1ea 35%, #cfd9b9 70%, #a9bd8a 100%);
  }
  .text-veil {
    position: absolute;
    left: 0;
    top: 440px;
    width: 1200px;
    height: 640px;
    background: linear-gradient(90deg, rgba(255,255,255,0.55) 0%, rgba(255,255,255,0.35) 55%, rgba(255,255,255,0) 85%);
  }
  .top-band {
    position: absolute;
    left: 0;
    top: 175px;
    width: 1200px;
    height: 180px;
    background: var(--navy);
  }
  .brand-box {
    position: absolute;
    left: 91px;
    top: 34px;
    width: 379px;
    height: 379px;
    box-sizing: border-box;
    background: var(--navy-deep);
    border: 4px solid var(--gold);
  }
  .brand-square {
    position: absolute;
    left: 30px;
    top: 150px;
    width: 68px;
    height: 68px;
    background: var(--gold);
  }
  .brand-name {
    position: absolute;
    left: 116px;
    top: 140px;
    margin: 0;
    color: var(--white);
    font-weight: 400;
    font-size: 35px;
    line-height: 42px;
    letter-spacing: 1px;
  }
  .brand-tagline {
    position: absolute;
    left: 118px;
    top: 232px;
    margin: 0;
    color: var(--white);
    font-weight: 400;
    font-size: 11px;
    letter-spacing: 2.4px;
  }
  .headline {
    position: absolute;
    left: 91px;
    top: 484px;
    margin: 0;
    color: var(--title);
    font-weight: 600;
    font-size: 47px;
    line-height: 60px;
  }
  .beneficiaries {
    position: absolute;
    left: 82px;
    top: 560px;
    margin: 0;
    padding: 0;
    list-style: none;
    color: var(--ink);
    font-weight: 400;
    font-size: 33px;
    line-height: 52px;
  }
</style>
</head>
<body>
  <main class="post">
    <div class="backdrop" role="img" aria-label="Foto desfocada de mãos entrelaçadas em gesto de apoio, com fundo claro e vegetação verde"></div>
    <div class="text-veil"></div>
    <div class="top-band"></div>

    <div class="brand-box">
      <div class="brand-square"></div>
      <p class="brand-name">VALADARES<br>MOREIRA</p>
      <p class="brand-tagline">SOCIEDADE DE ADVOCACIA</p>
    </div>

    <h1 class="headline">Pensão por Morte: quem tem direito?</h1>
    <ul class="beneficiaries">
      <li>- Cônjuges</li>
      <li>- Companheiro(a)</li>
      <li>- Filho(a), menor de 21 anos, não emancipado(a)</li>
      <li>- Filho(a), maior de 21 anos, inválido(a)</li>
      <li>- Enteado</li>
      <li>- Menor Tutelado</li>
      <li>- Pais</li>
      <li>- Irmão(ã), menor de 21 anos, não emancipado(a)</li>
      <li>- Irmão(ã), maior de 21 anos, inválido(a)</li>
      <li>- Companheira extraconjugal</li>
    </ul>
  </main>
</body>
</html>
```